Flyer für KFZ-Gutachter
Zielgruppe
NFZ und KFZ Gutachten. Firma ist neu gegründet und Flyer wird benötigt um sich bei Werkstätten, Versicherungen und Privatkunden vorzustellen.
Aufgabenstellung
Es soll elegant, klassisch sein und angelehnt sein an meine Website https://www.holvarentis.de/ Handynummer 0157 - 62830417 bitte einpflegen. Außerdem sollten die Logos des Bundesverbandes und der Zertifizierung mit im Flyer eingebunden werden. Diese lade ich hoch. Auch das korrekte Logo lade ich hoch.

```html
<!DOCTYPE html>
<html lang="de">
<head>
<meta charset="utf-8">
<title>Holvarentis – Flyer</title>
<link rel="stylesheet" href="https://fonts.googleapis.com/css2?family=Noticia+Text:wght@400;700&display=swap">
<style>
  :root{
    --backdrop:#e9e9e9;
    --paper-grey:#d3d3d3;
    --ink:#1b1b1b;
    --card:#efefef;
    --white:#ffffff;
    --photo-light:#6e6e6e;
    --photo-dark:#262626;
    --text-dark:#222222;
  }
  *{margin:0;padding:0;box-sizing:border-box}
  html,body{width:1200px;height:763px;overflow:hidden;background:var(--backdrop)}
  body{position:relative;font-family:"Noticia Text",Georgia,serif}
  .flyer{
    position:absolute;left:344px;top:20px;width:950px;height:1342px;
    transform:scale(.5387);transform-origin:0 0;
    background:var(--paper-grey);overflow:hidden;
  }
  .flyer-shapes{position:absolute;inset:0}
  .logo-block{
    position:absolute;left:290px;top:0;width:378px;height:328px;background:var(--ink);
    display:flex;flex-direction:column;align-items:center;justify-content:center;gap:26px;
  }
  .logo-square{width:54px;height:54px;border:3px solid var(--white)}
  .logo-name{color:var(--white);font-weight:700;font-size:44px;letter-spacing:2px}
  .headline{
    position:absolute;left:120px;top:482px;width:716px;text-align:center;
    color:var(--white);font-size:60px;font-weight:400;white-space:nowrap;
  }
  .headline-rule{position:absolute;left:553px;top:580px;width:283px;height:2px;background:var(--white)}
  .subline{
    position:absolute;right:113px;top:614px;text-align:right;color:var(--white);
    font-size:30px;line-height:36px;
  }
  .service-card{position:absolute;background:var(--card);text-align:center;padding-top:70px;color:var(--text-dark)}
  .service-card.is-raised{padding-top:90px}
  .service-card svg{display:block;margin:0 auto;height:52px}
  .service-title{font-size:18px;font-weight:700;margin-top:32px}
  .service-rule{width:92px;height:1.5px;background:var(--text-dark);margin:16px auto 20px}
  .service-text{font-size:12.5px;line-height:14.5px;text-align:left;padding:0 20px}
  .card-1{left:121px;top:775px;width:217px;height:343px}
  .card-2{left:367px;top:755px;width:218px;height:383px}
  .card-3{left:618px;top:775px;width:217px;height:343px}
  .phone-box{
    position:absolute;left:68px;top:1168px;width:320px;height:59px;background:var(--white);
    display:flex;align-items:center;gap:22px;padding-left:24px;color:var(--ink);font-size:35px;
  }
  .address{position:absolute;left:68px;top:1244px;color:var(--white);font-size:25px}
  .website{position:absolute;left:70px;top:1282px;color:var(--white);font-size:14px;letter-spacing:9px}
  .badge-strip{
    position:absolute;left:560px;top:1188px;width:390px;height:88px;background:var(--white);
    display:flex;align-items:center;gap:22px;padding-left:44px;
  }
  .badge-round{width:54px;height:54px;border-radius:50%;background:#3c6f9c}
  .badge-oval{width:80px;height:54px;border-radius:50%;background:#5b6f86}
  .badge-plate{width:110px;height:54px;background:#c9c9c9}
</style>
</head>
<body>
<main class="flyer">
  <svg class="flyer-shapes" viewBox="0 0 950 1342" width="950" height="1342">
    <defs>
      <linearGradient id="photoTone" x1="0" y1="0" x2="1" y2="0.3">
        <stop offset="0" stop-color="var(--photo-light)"/>
        <stop offset="0.55" stop-color="#4a4a4a"/>
        <stop offset="1" stop-color="var(--photo-dark)"/>
      </linearGradient>
    </defs>
    <polygon points="0,155 950,88 950,770 0,835" fill="url(#photoTone)" role="img" aria-label="Foto: Gutachter prüft mit Klemmbrett einen Motorraum in einer Werkstatt"/>
    <rect x="0" y="1095" width="950" height="247" fill="var(--ink)"/>
  </svg>

  <div class="logo-block">
    <span class="logo-square"></span>
    <span class="logo-name">HOLVARENTIS</span>
  </div>

  <h1 class="headline">Ihr Experte für Gutachten</h1>
  <span class="headline-rule"></span>
  <p class="subline">Präzise Bewertungen<br>für Ihre Bedürfnisse</p>

  <section class="service-card card-1">
    <svg viewBox="0 0 56 52" aria-hidden="true">
      <polygon points="20,2 24,10 32,6 28,14 36,16 26,20 18,18 14,10" fill="var(--ink)"/>
      <rect x="2" y="22" width="24" height="24" fill="var(--ink)"/>
      <path d="M30 44 V30 l6-8 h14 l4 8 v14 z" fill="var(--ink)"/>
      <circle cx="30" cy="44" r="5" fill="var(--card)" stroke="var(--ink)" stroke-width="3"/>
    </svg>
    <h2 class="service-title">Unfallgutachten</h2>
    <div class="service-rule"></div>
    <p class="service-text">Wir erstellen detaillierte Unfall-gutachten, die Ihnen bei der Schadensregulierung helfen und für Versicherungen präzise nachvollziehbar sind.</p>
  </section>

  <section class="service-card card-2 is-raised">
    <svg viewBox="0 0 56 44" aria-hidden="true">
      <path d="M6 20 L12 6 Q13 3 17 3 H39 Q43 3 44 6 L50 20 Q54 21 54 26 V38 H2 V26 Q2 21 6 20 Z" fill="var(--ink)"/>
      <path d="M12 19 L16 9 H40 L44 19 Z" fill="var(--card)"/>
      <circle cx="11" cy="28" r="3" fill="var(--card)"/><circle cx="45" cy="28" r="3" fill="var(--card)"/>
      <rect x="5" y="36" width="9" height="7" fill="var(--ink)"/><rect x="42" y="36" width="9" height="7" fill="var(--ink)"/>
    </svg>
    <h2 class="service-title">Wertgutachten</h2>
    <div class="service-rule"></div>
    <p class="service-text">Erhalten Sie fundierte Wertgut-achten, die Ihnen bei Kaufent-scheidungen oder bei der Schadenregulierung nützlich sein können.</p>
  </section>

  <section class="service-card card-3">
    <svg viewBox="0 0 56 52" aria-hidden="true">
      <g stroke="var(--ink)" stroke-width="2.5"><line x1="2" y1="4" x2="18" y2="14"/><line x1="4" y1="12" x2="18" y2="20"/><line x1="8" y1="20" x2="20" y2="26"/></g>
      <circle cx="26" cy="24" r="3" fill="var(--ink)"/>
      <rect x="34" y="18" width="18" height="30" fill="var(--ink)"/>
      <path d="M16 48 V38 l6-8 h16 v18 z" fill="var(--ink)"/>
      <circle cx="20" cy="47" r="4" fill="var(--card)" stroke="var(--ink)" stroke-width="3"/>
    </svg>
    <h2 class="service-title">Schadensgutachten</h2>
    <div class="service-rule"></div>
    <p class="service-text">Präzise Schadensgutachten, die alle relevanten Informationen enthalten und die rechtlichen Anforderungen erfüllen.</p>
  </section>

  <div class="phone-box">
    <svg width="30" height="30" viewBox="0 0 24 24" aria-hidden="true"><path fill="var(--ink)" d="M6.6 10.8a15.1 15.1 0 0 0 6.6 6.6l2.2-2.2c.3-.3.7-.4 1-.2 1.1.4 2.3.6 3.6.6.6 0 1 .4 1 1V20c0 .6-.4 1-1 1A17 17 0 0 1 3 4c0-.6.4-1 1-1h3.5c.6 0 1 .4 1 1 0 1.3.2 2.5.6 3.6.1.3 0 .7-.2 1z"/></svg>
    <span class="phone-number">0157 628 304 17</span>
  </div>
  <p class="address">Lindenweg 12 — 71088 Kesselfeld</p>
  <p class="website">WWW.HOLVARENTIS.DE</p>

  <div class="badge-strip" aria-label="Verbands- und Zertifizierungssiegel">
    <span class="badge-round"></span>
    <span class="badge-oval"></span>
    <span class="badge-plate"></span>
  </div>
</main>
</body>
</html>
```